Medical equipment business looking for professional, unique business card

We need a business card design for a durable medical equipment company. We are small but would like our cards to express that we are much bigger. We focus on braces (back, knee, wrist, etc) but also do crutches, rollators, wheelchairs- basically medical equipment that gets you going and back in Action. Our colors are blue and green and our logo has an arrow and use of a "spine". We'd like to express professionalism while being unique.

Industry/Entity Type

Medical Equipment

Contact Information for Business Card

Professional feel but unique. Memorable.

Font styles to use
Serif
Sans Serif
Other font styles liked:
• verdana

Requirements
Must have
• card holders cell#, business phone#, fax#, email, website address, business address, logo
Nice to have
• use of medical/healthcare related descriptive words, items, look
Should not have
• the wrong colors or cartoon characters.

```html
<!DOCTYPE html>
<html lang="en">
<head>
<meta charset="utf-8">
<title>Keystride Medical – Business Card</title>
<link href="https://fonts.googleapis.com/css2?family=Roboto:wght@400;500&family=Open+Sans:wght@600&display=swap" rel="stylesheet">
<style>
  :root {
    --navy: #0e4a72;
    --navy-deep: #0b3f63;
    --sky: #1f8fc9;
    --lime: #8cc63f;
    --ink: #4a4a4a;
    --paper: #ffffff;
    --backdrop: #e6e8ea;
  }
  * { margin: 0; padding: 0; box-sizing: border-box; }
  html, body {
    width: 1200px; height: 1000px; overflow: hidden;
    background: var(--backdrop);
    font-family: "Roboto", Arial, sans-serif;
  }
  .card {
    position: absolute; left: 220px; width: 760px;
    background: var(--paper);
    box-shadow: 0 2px 8px rgba(0,0,0,.18);
    overflow: hidden;
  }
  .card--front { top: 50px; height: 434px; }
  .card--back { top: 524px; height: 436px; }

  .brand {
    display: flex; align-items: center; gap: 18px;
    color: var(--navy);
    font-family: "Open Sans", Arial, sans-serif;
    font-weight: 600;
    white-space: nowrap;
  }
  .brand__dot { border-radius: 50%; background: var(--lime); flex: none; }

  .card--front .brand {
    position: absolute; top: 0; left: 0; right: 0; height: 380px;
    justify-content: center; font-size: 64px;
  }
  .card--front .brand__dot { width: 30px; height: 30px; }

  .product-band {
    position: absolute; left: 0; right: 0; bottom: 0; height: 54px;
    background: var(--navy-deep);
    display: flex; justify-content: center; align-items: center; gap: 9px;
    list-style: none; color: #fff; font-size: 17px;
  }
  .product-band li { display: flex; align-items: center; gap: 5px; }
  .product-band li::before {
    content: ""; width: 10px; height: 10px; border-radius: 50%; background: var(--lime);
  }

  .name-tab {
    position: absolute; left: 0; top: 43px; width: 13px; height: 43px;
    background: var(--lime); border-radius: 0 6px 6px 0;
  }
  .holder { position: absolute; left: 43px; top: 40px; }
  .holder__name { color: var(--sky); font-size: 23px; font-weight: 500; }
  .holder__title { color: var(--ink); font-size: 17px; margin-top: 2px; }

  .address {
    position: absolute; left: 43px; top: 203px;
    color: var(--ink); font-size: 17px; line-height: 22px; font-style: normal;
  }
  .contacts {
    position: absolute; left: 43px; top: 263px; list-style: none;
    color: var(--ink); font-size: 17px;
  }
  .contacts li { display: flex; align-items: center; gap: 7px; height: 24.5px; }
  .contacts svg { width: 13px; height: 13px; fill: var(--lime); flex: none; }

  .card--back .brand {
    position: absolute; left: 390px; top: 178px; font-size: 36px; gap: 12px;
  }
  .card--back .brand__dot { width: 18px; height: 18px; }

  .footer-band { position: absolute; left: 0; bottom: 0; width: 760px; height: 20px; }
</style>
</head>
<body>

<section class="card card--front">
  <div class="brand"><span class="brand__dot"></span>Keystride Medical</div>
  <ul class="product-band">
    <li>Back</li><li>Knee</li><li>Wrist</li><li>Crutches</li><li>Rollators</li><li>Wheelchairs</li>
  </ul>
</section>

<section class="card card--back">
  <span class="name-tab"></span>
  <div class="holder">
    <p class="holder__name">John Smith</p>
    <p class="holder__title">President</p>
  </div>

  <address class="address">Street name, Suite 100<br>State, Zip Code, Country</address>

  <ul class="contacts">
    <li><svg viewBox="0 0 16 16"><path d="M3 1l3 3-2 2c1 2 3 4 5 5l2-2 3 3-2 3C6 15 1 10 0 4z"/></svg>012 345 6789</li>
    <li><svg viewBox="0 0 16 16"><path d="M4 0h8v16H4zM5.5 2v10h5V2z"/></svg>012 345 6789</li>
    <li><svg viewBox="0 0 16 16"><path d="M4 1h8v4H4zM1 6h14v6h-3v3H4v-3H1zM5 10v3h6v-3z"/></svg>012 345 6789</li>
    <li><svg viewBox="0 0 16 16"><path d="M0 3h16v10H0zM1.5 4.5L8 9l6.5-4.5z"/></svg>info@yourwebsite.com</li>
    <li><svg viewBox="0 0 16 16"><path d="M8 0a8 8 0 100 16A8 8 0 008 0zm0 1.5c1 1 1.8 3 2 5.7H6c.2-2.7 1-4.7 2-5.7zM1.6 7.2C1.9 4.5 3.7 2.3 6 1.7 5.2 3 4.6 5 4.5 7.2zm9.9 0c-.1-2.2-.7-4.2-1.5-5.5 2.3.6 4.1 2.8 4.4 5.5zM1.6 8.8h2.9c.1 2.2.7 4.2 1.5 5.5-2.3-.6-4.1-2.8-4.4-5.5zm4.4 0h4c-.2 2.7-1 4.7-2 5.7-1-1-1.8-3-2-5.7zm5.5 0h2.9c-.3 2.7-2.1 4.9-4.4 5.5.8-1.3 1.4-3.3 1.5-5.5z"/></svg>www.yourwebsite.com</li>
  </ul>

  <div class="brand"><span class="brand__dot"></span>Keystride Medical</div>

  <svg class="footer-band" viewBox="0 0 760 20" aria-hidden="true">
    <polygon points="0,0 525,0 513,20 0,20" fill="var(--navy-deep)"/>
    <polygon points="530,0 760,0 760,20 518,20" fill="var(--lime)"/>
  </svg>
</section>

</body>
</html>
```